Improvements to a dating website design

Current site: http://vorilla.example:8079/pages/index.html

I am looking for an update to our current design that will be more engaging to our users. The current version feels a little too brash and business-like. I would like to make it feel more inviting, to women especially, but men as well. The site is aimed at Indians and other South Asians in their mid 20s to late 30s, living primarily in the U.S. and Canada. It is still under development and not yet live.

This redesign is for the public part of the site, and not the inside pages for member users. To be clear, the sections to be redesigned are:
- the home landing page
- How It Works
- FAQ
- About Us
- Sign Up

Please take the text from the site for the copy.

Thanks, and looking forward to seeing your designs!
Updates

Target Market(s)

Our users will be:
- South Asian (indian, Pakistani, Sri Lankan, etc.) single men and women
- in their mid 20s to late 30s
- living primarily in the U.S. and Canada

Industry/Entity Type

Dating

Coding

Coded - Design and coding required

Number of Pages Required

1 page

Requirements
Must have
• I am updating the requirements for this to be a coded HTML/CSS page. (I've also increased the budget, added a 2nd place prize, extended the deadline, and guaranteed payment.) The design should be suitable for "responsiveness" to different browser window sizes, down to mobile phones.
• The main image, which is attached in the files, should continue to be the main image. However, the image can be re-cropped and re-filtered to better match the design. I am happy with the image being used as a full-page backdrop on the home page area, but I'm open to changes.
• All of the text on the current site should be part of the updated design. However, it can be reformatted and laid out differently. (Headings and navigation can be different.)
• The 'What's a Mingle Night?' section should have the sentences broken out from the single paragraph so that it is easier to read. Each sentence can be a distinct item.
Nice to have
• This site is about online events (called 'Mingle Nights') where users can meet and get to know each other. So please keep in mind that the point of the website is to
• - educate users how Mingle Nights work
• - get them to purchase a reservation for the next Mingle Night (which will be the first).
• Also, the design does not have to be completely different from the existing design, as the site is not yet live and has not been seen by users. Incremental, even small, changes to the current site that result in a captivating design would be just fine.
• Please consider using colors other than the logo colors.
Should not have
• It is not easy to find the right photo, so if you put additional images of people in your design, please make sure they
• - look South Asian (Indian, Pakistani, Sri Lankan, etc.)
• - are wearing western clothing in a western setting
• Also, any images must be available for rights-free licensing. I can't accept submissions that don't follow these guidelines.
• This site is not like other dating sites, in that it has no profiles for users to go through and see. So please don't include any samples of these. Also, no testimonials, as this is a new site.
• There should not be any hearts in the design!
• Any iconified version of the word 'Vorilla' must be either the actual full-color logo, or a monochrome version of it. Please don't use other word shapes for the site name.

```html
<!DOCTYPE html>
<html lang="en">
<head>
<meta charset="utf-8">
<title>Vorilla – Mingle Nights</title>
<link href="https://fonts.googleapis.com/css2?family=Open+Sans:wght@400;600;700&family=Montserrat:wght@600;700;800&display=swap" rel="stylesheet">
<style>
:root{
  --magenta:#b0107c;
  --magenta-dark:#8a0a61;
  --red:#e3191f;
  --ink:#1d1b20;
  --ink-2:#2a262c;
  --text:#555;
  --white:#fff;
  --line:#c9c2c7;
}
*{box-sizing:border-box;margin:0;padding:0}
html,body{width:1200px;height:2668px;overflow:hidden}
body{font-family:"Open Sans",Arial,sans-serif;color:var(--text);background:var(--white);position:relative}
.btn{display:inline-block;background:var(--magenta);color:var(--white);font:700 13px "Open Sans",sans-serif;letter-spacing:.5px;padding:11px 26px;text-transform:uppercase;white-space:nowrap}

/* hero */
.hero{position:absolute;left:0;top:0;width:1200px;height:720px;overflow:hidden}
.hero-photo{position:absolute;inset:0;background:
  radial-gradient(ellipse at 40% 35%,rgba(210,170,120,.55),transparent 55%),
  linear-gradient(180deg,#8c8a86 0%,#6d6b6a 35%,#4a4644 70%,#2f2b2a 100%)}
.nav{position:absolute;left:0;top:0;width:100%;height:80px;display:flex;align-items:center;justify-content:space-between;padding:0 40px 0 42px}
.logo{font:800 52px "Montserrat",sans-serif;color:var(--magenta);letter-spacing:-1px}
.menu{display:flex;gap:34px;list-style:none}
.menu li{font:600 13px "Open Sans",sans-serif;color:var(--white);padding-bottom:6px;white-space:nowrap}
.menu li.active{border-bottom:3px solid var(--magenta)}
.story{position:absolute;left:330px;top:96px;width:540px;height:290px;background:rgba(20,16,20,.72);text-align:center;color:var(--white);padding:30px 40px}
.story h1{font:700 32px "Montserrat",sans-serif;color:var(--magenta);letter-spacing:2px;margin-bottom:22px}
.story p{font-size:16px;line-height:1.45}
.pitch{position:absolute;left:260px;top:406px;width:680px;text-align:center;color:var(--white);font-size:17px;line-height:1.5}
.pitch p+p{margin-top:14px}
.pitch .lead{color:#f06ac4;font-weight:600}

/* login bar */
.login{position:absolute;left:0;top:720px;width:1200px;height:76px;background:var(--ink);display:flex;align-items:center;padding:0 40px 0 60px;color:var(--white)}
.login label{font:700 22px "Open Sans",sans-serif;margin-right:14px;white-space:nowrap}
.login .field{width:300px;height:30px;background:var(--white);border-radius:2px;font-size:11px;color:#999;padding:8px 10px;margin-right:44px;white-space:nowrap}
.login .pw{position:relative}
.login .pw small{position:absolute;left:0;top:36px;font-size:11px;color:#ccc}
.login .btn{padding:12px 36px}

/* what is */
.about-event{position:absolute;left:0;top:796px;width:1200px;height:250px;text-align:center;padding-top:30px}
.section-title{font:700 34px "Montserrat",sans-serif;color:var(--magenta)}
.event-points{list-style:none;width:860px;margin:12px auto 14px}
.event-points li{font-size:13px;line-height:18px;color:#666}
.event-points li+li{margin-top:1px}

/* how it works */
.how{position:absolute;left:0;top:1046px;width:1200px;height:820px;background:#fafafa}
.how .section-title{text-align:center;margin-top:26px}
.how svg.links{position:absolute;left:0;top:0}
.diamond{position:absolute;width:196px;height:196px;transform:rotate(45deg);background:var(--magenta);border-radius:18px;box-shadow:0 6px 14px rgba(0,0,0,.18)}
.diamond.first{background:var(--red)}
.step{position:absolute;width:200px;text-align:center;color:var(--white);font-size:11.5px;line-height:1.5}
.step .icon{width:48px;height:48px;border-radius:50%;background:var(--white);margin:0 auto 10px;display:flex;align-items:center;justify-content:center}
.step .btn{background:var(--white);color:var(--magenta);font-size:11px;padding:7px 16px;margin-top:10px}
.step.first .btn{color:var(--red)}

/* join band */
.join{position:absolute;left:0;top:1866px;width:1200px;height:148px;background:linear-gradient(90deg,#3a1a2e 0%,#8a2f5c 35%,#c85a7c 55%,#7a2a50 80%,#2a1422 100%);display:flex;align-items:center;justify-content:center;gap:140px}
.join .cta{width:300px;height:64px;display:flex;align-items:center;justify-content:center;gap:14px;font:600 22px "Open Sans",sans-serif;border-radius:3px}
.join .signin{background:rgba(255,255,255,.92);color:var(--magenta)}
.join .signup{background:var(--magenta);color:var(--white);border:2px solid rgba(255,255,255,.6)}

/* faq & about */
.info{position:absolute;left:0;top:2014px;width:1200px;height:420px;background:var(--ink-2);display:flex;padding:40px 60px 0 60px;color:#ddd}
.faq{width:560px}
.info h2{font:700 30px "Montserrat",sans-serif;color:var(--magenta);margin-bottom:18px}
.faq ul{list-style:none}
.faq li{display:flex;align-items:center;gap:12px;font-size:15px;margin-bottom:16px}
.faq li.open{color:var(--magenta)}
.tick{width:16px;height:16px;background:#ddd;border-radius:2px;flex:none;display:flex;align-items:center;justify-content:center}
.about{width:520px;margin-left:60px}
.about p{font-size:13px;line-height:1.7;margin-bottom:24px}

/* contact */
.contact{position:absolute;left:0;top:2434px;width:1200px;height:150px;background:var(--magenta);color:var(--white);padding:28px 80px}
.contact .row{display:flex;align-items:center;gap:14px;font:600 20px "Open Sans",sans-serif}
.contact .row+.row{margin-top:30px}
.contact .item{display:flex;align-items:center;gap:14px;width:340px;white-space:nowrap}
.footer{position:absolute;left:0;top:2584px;width:1200px;height:84px;background:#2a1224;color:#ccc;display:flex;align-items:center;justify-content:center;font-size:11px}
.social{position:absolute;right:40px;top:30px;display:flex;gap:8px}
.social span{width:24px;height:24px;background:var(--white)}
</style>
</head>
<body>

<header class="hero">
  <div class="hero-photo" role="img" aria-label="Smiling young woman with a backpack on a busy city street, taxis and scaffolding behind her"></div>
  <nav class="nav">
    <div class="logo">vorilla</div>
    <ul class="menu">
      <li class="active">HOME</li><li>HOW IT WORKS</li><li>ABOUT US</li><li>FAQS</li><li>SIGN IN</li>
    </ul>
  </nav>
  <div class="story">
    <h1>CHEMISTRY</h1>
    <p>That little sizzle in your gut when you meet.</p>
    <p>The cheerful banter where the words just flow.</p>
    <p>That mysterious, undeniable, necessary connection.</p>
  </div>
  <div class="pitch">
    <p>Will you actually get along together? Do you agree on the important things?<br>Would your family like them?</p>
    <p>It seems so hopelessly complicated, and it takes so much time.<br>We understand. And we've got the perfect answer.</p>
    <p class="lead">Learn about Mingle Nights and meet the one who clicks.</p>
  </div>
</header>

<section class="login">
  <label>Email :</label><div class="field">Enter your Email</div>
  <label>Password:</label><div class="field pw">Enter your Password<small>Forgot your password?</small></div>
  <span class="btn">SIGN UP</span>
</section>

<section class="about-event">
  <h2 class="section-title">What's a Mingle Night?</h2>
  <ul class="event-points">
    <li>It's a fully online speed-meeting event for the digital age.</li>
    <li>We ask you some simple questions about who you are and what you are looking for.</li>
    <li>You choose a time that suits you.</li>
    <li>On the evening we match you with singles who share your values, and you chat one to one in short rounds.</li>
    <li>Nothing to browse, no profiles to judge.</li>
    <li>Just real conversation.</li>
  </ul>
  <span class="btn">READ MORE</span>
</section>

<section class="how">
  <h2 class="section-title">How It Works</h2>
  <svg class="links" width="1200" height="820" viewBox="0 0 1200 820" aria-hidden="true">
    <g stroke="var(--line)" stroke-width="2" fill="none">
      <line x1="252" y1="300" x2="1048" y2="300"/>
      <line x1="640" y1="300" x2="640" y2="420"/>
      <line x1="472" y1="360" x2="472" y2="420"/>
      <line x1="880" y1="360" x2="880" y2="420"/>
      <line x1="472" y1="420" x2="880" y2="420"/>
    </g>
  </svg>

  <div class="diamond first" style="left:154px;top:202px"></div>
  <div class="diamond" style="left:542px;top:136px"></div>
  <div class="diamond" style="left:950px;top:136px"></div>
  <div class="diamond" style="left:374px;top:456px"></div>
  <div class="diamond" style="left:782px;top:456px"></div>

  <div class="step first" style="left:152px;top:222px">
    <div class="icon"><svg width="22" height="26" viewBox="0 0 22 26"><rect x="2" y="1" width="18" height="24" rx="2" fill="none" stroke="var(--red)" stroke-width="2"/><line x1="6" y1="9" x2="16" y2="9" stroke="var(--red)" stroke-width="2"/><line x1="6" y1="14" x2="16" y2="14" stroke="var(--red)" stroke-width="2"/><line x1="6" y1="19" x2="13" y2="19" stroke="var(--red)" stroke-width="2"/></svg></div>
    When you sign up, you will answer a few questions so we can match you with singles who fit.
    <br><span class="btn">READ MORE</span>
  </div>
  <div class="step" style="left:540px;top:156px">
    <div class="icon"><svg width="24" height="24" viewBox="0 0 24 24"><circle cx="12" cy="8" r="5" fill="var(--magenta)"/><path d="M2 23c1-6 5-9 10-9s9 3 10 9z" fill="var(--magenta)"/></svg></div>
    Then, at the time of the event, you will log in to the Mingle Night from your own computer.
    <br><span class="btn">READ MORE</span>
  </div>
  <div class="step" style="left:948px;top:156px">
    <div class="icon"><svg width="24" height="22" viewBox="0 0 24 22"><rect x="1" y="1" width="22" height="20" rx="2" fill="none" stroke="var(--magenta)" stroke-width="2"/><path d="M4 18l6-7 4 4 3-3 4 6z" fill="var(--magenta)"/></svg></div>
    Once logged in, you will chat with each match you are given, one short round at a time.
    <br><span class="btn">READ MORE</span>
  </div>
  <div class="step" style="left:372px;top:476px">
    <div class="icon"><svg width="24" height="24" viewBox="0 0 24 24"><circle cx="8" cy="8" r="4" fill="var(--magenta)"/><circle cx="17" cy="8" r="4" fill="var(--magenta)"/><path d="M1 22c1-5 4-8 7-8s6 3 7 8zM11 22c1-5 3-8 6-8s5 3 6 8z" fill="var(--magenta)"/></svg></div>
    While you chat, pick who you would like to see again. Each round lasts twelve minutes.
    <br><span class="btn">READ MORE</span>
  </div>
  <div class="step" style="left:780px;top:476px">
    <div class="icon"><svg width="24" height="24" viewBox="0 0 24 24"><circle cx="12" cy="12" r="10" fill="none" stroke="var(--magenta)" stroke-width="2"/><path d="M7 12l3 3 7-7" fill="none" stroke="var(--magenta)" stroke-width="2.5"/></svg></div>
    Finally, you will see which of your choices picked you too, and the two of you can keep talking.
    <br><span class="btn">READ MORE</span>
  </div>
</section>

<section class="join">
  <div class="cta signin"><svg width="20" height="20" viewBox="0 0 20 20"><path d="M8 4l6 6-6 6M14 10H2" fill="none" stroke="var(--magenta)" stroke-width="2.4"/></svg>Sign In</div>
  <div class="cta signup"><svg width="20" height="20" viewBox="0 0 20 20"><circle cx="10" cy="6" r="4" fill="var(--white)"/><path d="M2 19c1-5 4-7 8-7s7 2 8 7z" fill="var(--white)"/></svg>Sign Up <svg width="18" height="14" viewBox="0 0 18 14"><path d="M10 1l6 6-6 6M16 7H1" fill="none" stroke="var(--white)" stroke-width="2"/></svg></div>
</section>

<section class="info">
  <div class="faq">
    <h2>FAQ</h2>
    <ul>
      <li class="open"><span class="tick" style="background:var(--magenta)"></span>What are Mingle Nights?</li>
      <li><span class="tick"><svg width="10" height="10" viewBox="0 0 10 10"><path d="M1 5l3 3 5-6" fill="none" stroke="var(--ink-2)" stroke-width="2"/></svg></span>What are the technology requirements to be able to take part in the event?</li>
      <li><span class="tick"><svg width="10" height="10" viewBox="0 0 10 10"><path d="M1 5l3 3 5-6" fill="none" stroke="var(--ink-2)" stroke-width="2"/></svg></span>Is it possible to test my system to see if it will work in the event?</li>
      <li><span class="tick"><svg width="10" height="10" viewBox="0 0 10 10"><path d="M1 5l3 3 5-6" fill="none" stroke="var(--ink-2)" stroke-width="2"/></svg></span>What will other users see about me?</li>
      <li><span class="tick"><svg width="10" height="10" viewBox="0 0 10 10"><path d="M1 5l3 3 5-6" fill="none" stroke="var(--ink-2)" stroke-width="2"/></svg></span>How long does the profile questionnaire take?</li>
      <li><span class="tick"><svg width="10" height="10" viewBox="0 0 10 10"><path d="M1 5l3 3 5-6" fill="none" stroke="var(--ink-2)" stroke-width="2"/></svg></span>Does a MATCH who doesn't choose me back know that I picked them?</li>
      <li><span class="tick"><svg width="10" height="10" viewBox="0 0 10 10"><path d="M1 5l3 3 5-6" fill="none" stroke="var(--ink-2)" stroke-width="2"/></svg></span>Will you match me with people close by?</li>
    </ul>
  </div>
  <div class="about">
    <h2>About Us</h2>
    <p>We started Vorilla because meeting the right person should not feel like a chore. Too many of our friends spent years scrolling through profiles that never told them what mattered. So we built something different: live online evenings where South Asian singles across the U.S. and Canada can simply talk. We match people on shared values, family outlook and goals, then step aside and let the conversation happen. No endless browsing, no pressure, just a real chance to find that spark with someone who truly understands you.</p>
    <span class="btn">READ MORE</span>
  </div>
</section>

<section class="contact">
  <div class="row">
    <div class="item"><svg width="22" height="22" viewBox="0 0 22 22"><path d="M5 1l4 5-2 3c1 3 3 5 6 6l3-2 5 4-3 4C9 21 1 13 1 4z" fill="var(--white)"/></svg>555.010.2468</div>
    <div class="item"><svg width="22" height="22" viewBox="0 0 22 22"><rect x="5" y="1" width="12" height="20" rx="2" fill="none" stroke="var(--white)" stroke-width="2"/><circle cx="11" cy="17" r="1.4" fill="var(--white)"/></svg>555.010.2468</div>
    <div class="item"><svg width="24" height="18" viewBox="0 0 24 18"><rect x="1" y="1" width="22" height="16" fill="none" stroke="var(--white)" stroke-width="2"/><path d="M1 1l11 9 11-9" fill="none" stroke="var(--white)" stroke-width="2"/></svg>hello@vorilla.example</div>
  </div>
  <div class="row">
    <div class="item" style="width:auto"><svg width="18" height="24" viewBox="0 0 18 24"><path d="M9 1a8 8 0 0 1 8 8c0 6-8 14-8 14S1 15 1 9a8 8 0 0 1 8-8z" fill="var(--white)"/><circle cx="9" cy="9" r="3" fill="var(--magenta)"/></svg>12 Harbor Lane, Suite 4, - 540210, Canada</div>
  </div>
</section>

<footer class="footer">
  All Rights Reserved. Copyright 2016 Vorilla
  <div class="social"><span></span><span></span><span></span></div>
</footer>

</body>
</html>
```